What's Needed:
- All designs files created
- Fully coded implementation in HTML/CSS/Bootstrap
- Pages: 5 -- see content here http://www.TeamPrismly.com
-- Home Page
-- The Hidden Value
-- Benefits
-- About us
-- Careers
- The existing site has the textual content for each page. We can tweak to meet specific designs if needed.
- You will need to update/create image and interactive content for pages.

Reference:
Our existing website has a lot of content on it for reference -
http://www.TeamPrismly.com

Description:
We need a web design that focuses in the UX and conveys the idea of magically fixing company problems by way of using our software.

Home Page
The main goal is to Drive Sales of the SaaS tool. When a visitor lands on our home page they should see: What we do, How we can help their problem and How to contact us.
1. Quickly understand What We Do
-- we sell SaaS software.
-- Need to quickly convey what our software does. It's seems complicated but really its not. See the description in about us for more info and visit our existing site.

2. How we can help their problem
-- We aim to solve any problem related to employees
-- Even if the visitor does not have a specific problem in mind, there are several areas organizations can always improve: (some examples below)
---- Create Stronger, More Productive Teams
---- Build Better Communications Pathways
---- Encourage Innovation and Positive Change
---- Develop and Retain Strong "Company Culture"

3. Be able to Contact Us to get started
-- contacting us to get a sales lead is the ultimate goal.
-- the user should not have to hunt to contact us. needs to be easy.

Other Pages (Hidden Value, Benefit, About Us, Careers):
-- These are informative pages about our software and process.
-- If we grab the attention of the user on the home page then these are the pages that they will explore for more info.
-- Should be able to link to these pages from the main nav or from sections with the homepage. For example: What We Do sections could link to the benefits page. How we help their problem sections could link to the Hidden Value page. Regardless of what links to where, the idea is that we will be able to nav to other areas.

About Us:
Our company name is TeamPrismly (as in Organizational Analysis). We provide a software as a service (SaaS) that uses a simple 6-question survey to analyze the relationships of people within an Organization and provide leaders with ground-breaking Insights about their teams, interactive social network data visualizations to explore their team's composition and we give detailed profiles of the key players (i.e, who are the Social Bridges, Who are the Knowledge Bottlenecks, Who are the Best Mentors, Who are the people that are completely disconnected/out of the loop). Leaders then use this information to make high level organizational decisions.

What's unique about our software:
-- Powerful analysis results from just a 6-question "pulse-surveys"
-- Innovative Tools for visually exploring the organization through relationships as opposed to org-chart
-- Get real-time results as opposed to waiting months with traditional methods
-- Traditional Org-charts represent the organization's skeleton, whereas we uncover the organization's neural network (how it solves problems).

Preferred fonts (but could be convinced otherwise if looks great):
-- Section titles - Aleo
-- Main body - Lato
-- TeamPrismly logo - Philosopher

Things we like:
-- We like a big slider as the top of the landing page.

Colors to include:
-- Colors in the logo (red, blue, green, teal) as accent colors

Feel of the site:
-- Cutting-edge Software
-- Professional
-- Social Network flare (we analyze relationships)

Note:
If we find a great match with a designer there is strong possibility to continue the relationship with follow on work redesigning our web-based application.

Target Market(s)

Current customers are Harwell Pike & Morrow, Copperline Trust Bank.
We target anyone that manages a large team. Such as Corporate Leaders, High Level Managers, HR Leaders

Industry/Entity Type

Business Software

Contact Information for Business Card

Logo image
Name of company "TEAMPRISMLY" In Philosopher font.
Tagline: "Reveal the Quiet Strength Of Every Crew"
Person's Name, Title, email, phone.

Coding

Coded - Design and coding required

Number of Pages Required

4 page

Font styles to use
Other font styles liked:
• Lato, Philosopher, Aero

Colors
ec1f27
0255a3

Requirements
Must have
• See description.
Nice to have
• Things we like:
• We like a big slider as the top of the landing page. Ours is a little clunky and outdated but something fresh and sleek would be great.
• Colors to include:
• We would like to use the colors in the logo as accent colors in the site to give a consistent look and feel.
• Feel of the site:
• Cutting-edge Software
• Professional
• Social Network flare (we analyze relationships)

```html
<!DOCTYPE html>
<html lang="en">
<head>
<meta charset="utf-8">
<title>TeamPrismly — Home</title>
<link href="https://fonts.googleapis.com/css2?family=Roboto+Slab:wght@300;400&family=Arimo:wght@400&display=swap" rel="stylesheet">
<style>
:root{
  --green:#a3c63a;
  --red:#e52229;
  --teal:#66c6e6;
  --lime:#a9cc3a;
  --navy:#2f3f95;
  --heading:#4f4f4f;
  --text:#666;
  --muted:#8a8a8a;
  --light-bg:#f4f5f7;
  --line:#e3e3e3;
  --footer:#3c3c3c;
  --white:#fff;
}
*{margin:0;padding:0;box-sizing:border-box}
html,body{width:1200px;height:2387px;overflow:hidden;background:var(--white)}
body{position:relative;font-family:"Arimo",Arial,sans-serif;color:var(--text)}
.abs{position:absolute}
.slab{font-family:"Roboto Slab",Georgia,serif}

/* header */
.site-header{left:0;top:0;width:1200px;height:106px;background:var(--white);box-shadow:0 1px 4px rgba(0,0,0,.12);z-index:2}
.brand{left:86px;top:30px;display:flex;align-items:center;gap:10px}
.brand-dot{width:26px;height:26px;border-radius:50%;background:var(--red)}
.brand-name{font-family:"Roboto Slab",Georgia,serif;font-size:20px;color:var(--navy);letter-spacing:1px}
.top-contact{top:18px;display:flex;align-items:center;gap:12px;font-family:"Roboto Slab",serif;font-size:14px;color:var(--green)}
.top-contact .ring{width:36px;height:36px;border:1px solid var(--green);border-radius:50%;display:flex;align-items:center;justify-content:center}
.main-nav{top:70px;right:85px;display:flex;gap:50px;font-family:"Roboto Slab",serif;font-size:13px;color:#333}

/* hero */
.hero{left:0;top:106px;width:1200px;height:475px;background:linear-gradient(100deg,#f6f3ef 0%,#eee6dc 30%,#d9c3a6 45%,#b9cfe0 62%,#7fa2c4 85%,#5f87b0 100%)}
.hero-title{left:86px;top:138px;font-family:"Roboto Slab",serif;font-weight:300;font-size:38px;color:#555;letter-spacing:1px}
.hero-text{left:86px;top:200px;width:330px;font-family:"Roboto Slab",serif;font-size:15px;line-height:28px;color:#777}
.hero-btn{left:86px;top:304px;width:114px;height:36px;border:1px solid #bbb;border-radius:3px;font-family:"Roboto Slab",serif;font-size:14px;color:#888;display:flex;align-items:center;justify-content:center;background:rgba(255,255,255,.3)}
.slider-dots{left:92px;top:448px;display:flex;gap:6px}
.slider-dots span{width:12px;height:12px;border-radius:50%;border:1px solid #aaa}
.slider-dots .active{border-color:var(--red);border-width:2px}

/* section headings */
.section-title{left:0;width:1200px;text-align:center;font-family:"Roboto Slab",serif;font-size:22px;color:var(--heading)}
.section-sub{left:0;width:1200px;text-align:center;font-family:"Roboto Slab",serif;font-weight:300;font-size:13px;color:var(--muted)}

/* what we do */
.service{width:240px;text-align:center}
.service-icon{width:102px;height:102px;border-radius:50%;margin:0 auto;display:flex;align-items:center;justify-content:center;box-shadow:0 0 0 3px #fff,0 0 0 4px #ddd}
.service-name{margin-top:20px;font-family:"Roboto Slab",serif;font-size:16px;color:#444}
.service-desc{margin-top:10px;font-size:12px;line-height:22px;color:var(--muted)}

/* about */
.about{left:0;top:966px;width:1200px;height:435px;background:var(--light-bg)}
.about-title{left:86px;top:1002px;font-family:"Roboto Slab",serif;font-size:22px;color:var(--heading)}
.about-text{left:86px;top:1046px;width:540px;font-size:12px;line-height:25px;color:#555}
.unique-title{left:86px;top:1176px;font-family:"Roboto Slab",serif;font-size:15px;color:var(--green)}
.unique-list{left:86px;top:1214px;list-style:none;font-size:12px;color:#555}
.unique-list li{height:36px;display:flex;align-items:flex-start;gap:14px}
.unique-list li::before{content:"";width:8px;height:8px;margin-top:2px;border:2px solid var(--green);border-radius:50%;flex:none}
.about-visual{left:652px;top:995px;width:462px;height:374px;border-radius:6px;background:radial-gradient(ellipse at 50% 40%,#fdfdfd 0%,#eceef2 55%,#dcdfe4 100%)}

/* help */
.help-item{display:flex;gap:28px;width:330px}
.help-icon{width:76px;height:76px;border-radius:50%;border:1px solid var(--line);display:flex;align-items:center;justify-content:center;flex:none;background:#fff}
.help-text{padding-top:10px;font-family:"Roboto Slab",serif;font-size:13px;line-height:20px;color:#444;width:200px}
.help-link{margin-top:6px;display:flex;align-items:center;gap:8px;font-family:"Arimo",sans-serif;font-size:12px;color:var(--green);text-decoration:underline}

/* contact */
.contact{left:0;top:1878px;width:1200px;height:446px;background:var(--light-bg)}
.map{left:86px;top:2022px;width:495px;height:255px;background:linear-gradient(135deg,#f1e9c8 0%,#efe6b8 40%,#c9dfb7 60%,#b9d2ea 100%)}
.contact-intro{left:622px;top:2020px;width:470px;font-size:12px;line-height:22px;color:#444}
.contact-head{font-family:"Roboto Slab",serif;font-size:15px;color:#444}
.contact-line{font-size:12px;line-height:21px;color:var(--muted)}
.social{left:868px;top:2240px;display:flex;gap:8px}
.social span{width:35px;height:35px;border-radius:50%;border:1px solid #aaa}

.site-footer{left:0;top:2324px;width:1200px;height:63px;background:var(--footer);display:flex;align-items:center;justify-content:center;font-size:12px;color:#eee}
</style>
</head>
<body>

<header class="abs site-header">
  <div class="abs brand"><span class="brand-dot"></span><span class="brand-name">TEAMPRISMLY</span></div>
  <div class="abs top-contact" style="left:636px">
    <span class="ring"><svg width="16" height="16" viewBox="0 0 24 24" fill="none" stroke="#a3c63a" stroke-width="2"><path d="M5 3h4l2 5-3 2a11 11 0 0 0 6 6l2-3 5 2v4a2 2 0 0 1-2 2A17 17 0 0 1 3 5a2 2 0 0 1 2-2z"/></svg></span>
    <span>CALL US : (000)-121-1231</span>
  </div>
  <div class="abs top-contact" style="left:858px">
    <span class="ring"><svg width="16" height="16" viewBox="0 0 24 24" fill="none" stroke="#a3c63a" stroke-width="2"><rect x="3" y="5" width="18" height="14" rx="1"/><path d="M3 6l9 7 9-7"/></svg></span>
    <span>EMAIL : info@teamprismly.com/</span>
  </div>
  <nav class="abs main-nav"><span>HOME</span><span>ABOUT US</span><span>WHAT WE DO</span><span>HOW WE CAN HELP</span><span>CONTACT US</span></nav>
</header>

<section class="abs hero" role="img" aria-label="Photo of hands working on analytics charts at a laptop with data overlay graphics">
  <h1 class="abs hero-title">TEAMPRISMLY</h1>
  <p class="abs hero-text">Our company name is TeamPrismly We provide a software as a service (SaaS) that survey to analyze the relationships</p>
  <div class="abs hero-btn">READ MORE</div>
  <div class="abs slider-dots"><span></span><span class="active"></span><span></span></div>
</section>

<h2 class="abs section-title" style="top:638px">WHAT WE DO</h2>
<p class="abs section-sub" style="top:680px">Our automated algorithms provide insights into the roles individuals play within the team beyond their titles.</p>

<div class="abs service" style="left:90px;top:729px">
  <div class="service-icon" style="background:var(--red)"><svg width="50" height="44" viewBox="0 0 50 44" fill="none" stroke="#fff" stroke-width="2.5"><rect x="3" y="4" width="40" height="32"/><line x1="3" y1="11" x2="43" y2="11"/><line x1="10" y1="18" x2="24" y2="18"/><line x1="10" y1="24" x2="30" y2="24"/><line x1="10" y1="30" x2="26" y2="30"/><path d="M32 34l12-14 4 4-12 14h-4z"/></svg></div>
  <div class="service-name">On Line Pulse Survey</div>
  <p class="service-desc">Our automated algorithms provide insights within the team beyond their titles.</p>
</div>
<div class="abs service" style="left:348px;top:729px">
  <div class="service-icon" style="background:var(--teal)"><svg width="50" height="44" viewBox="0 0 50 44" fill="none" stroke="#fff" stroke-width="2.5"><rect x="6" y="24" width="7" height="16"/><rect x="18" y="18" width="7" height="22"/><rect x="30" y="26" width="7" height="14"/><path d="M6 16l12-8 12 6 14-10"/></svg></div>
  <div class="service-name">Proprietary&nbsp; Algorithms</div>
  <p class="service-desc">Our automated algorithms provide insights within the team beyond their titles.</p>
</div>
<div class="abs service" style="left:606px;top:729px">
  <div class="service-icon" style="background:var(--lime)"><svg width="50" height="44" viewBox="0 0 50 44" fill="#fff" stroke="#fff" stroke-width="2.5"><rect x="19" y="3" width="12" height="10"/><rect x="3" y="30" width="12" height="10"/><rect x="19" y="30" width="12" height="10"/><rect x="35" y="30" width="12" height="10"/><path fill="none" d="M25 13v9M9 30v-8h32v8M25 22v8"/></svg></div>
  <div class="service-name">Organizational Key Insights</div>
  <p class="service-desc">Our automated algorithms provide insights within the team beyond their titles.</p>
</div>
<div class="abs service" style="left:864px;top:729px">
  <div class="service-icon" style="background:var(--navy)"><svg width="50" height="44" viewBox="0 0 50 44" fill="none" stroke="#fff" stroke-width="2.5"><path d="M10 22h10l8-10 6 4-4 6h10v14H16l-6-4z"/><path d="M30 6l4-3M36 10l5-2"/></svg></div>
  <div class="service-name">Expert Review &amp; Action</div>
  <p class="service-desc">Our automated algorithms provide insights within the team beyond their titles.</p>
</div>

<section class="abs about"></section>
<h2 class="abs about-title">ABOUT US</h2>
<p class="abs about-text">Our company name is TeamPrismly (as in Organizational Analysis). We provide a softwareas a service (SaaS) that uses a simple 6-question survey to analyze the relationships of people within and Organization and provide leaders with ground-breaking Insights about their teams, interactive social use this information to make high level organizational decisions.</p>
<h3 class="abs unique-title">What's unique about our software:</h3>
<ul class="abs unique-list">
  <li>Powerful analysis results from just a 6-question "pulse-surveys</li>
  <li>Innovative Tools for visually exploring the organization through relationships as opposed</li>
  <li>Get real-time results as opposed to waiting months with traditional methods</li>
  <li>Get real-time results as opposed to waiting months with traditional methods</li>
</ul>
<div class="abs about-visual" role="img" aria-label="Desktop monitor and tablet showing a colourful social network visualization of team relationships"></div>

<h2 class="abs section-title" style="top:1456px">HOW WE CAN HELP THEIR PROBLEM</h2>
<p class="abs section-sub" style="top:1500px">Our automated algorithms provide insights into the roles individuals play within the team beyond their titles.</p>

<div class="abs help-item" style="left:86px;top:1579px">
  <div class="help-icon"><svg width="30" height="24" viewBox="0 0 30 24" fill="#bbb"><circle cx="15" cy="7" r="5"/><circle cx="6" cy="9" r="3.5"/><circle cx="24" cy="9" r="3.5"/><path d="M6 22a9 9 0 0 1 18 0z"/><path d="M0 22a6 6 0 0 1 8-6l-2 6zM30 22a6 6 0 0 0-8-6l2 6z"/></svg></div>
  <div><div class="help-text">We aim to solve any problem related to employees</div><div class="help-link">CLICK HERE FOR MORE INFO <svg width="11" height="11" viewBox="0 0 12 12" fill="none" stroke="#a3c63a" stroke-width="1.5"><circle cx="6" cy="6" r="5"/><path d="M5 4l2 2-2 2"/></svg></div></div>
</div>
<div class="abs help-item" style="left:454px;top:1579px">
  <div class="help-icon"><svg width="26" height="26" viewBox="0 0 26 26" fill="none" stroke="#aaa" stroke-width="1.8"><path d="M24 2L2 11l9 4 4 9z"/><path d="M11 15L24 2"/></svg></div>
  <div><div class="help-text">Even if the visitor does not have a specific problem in mind</div><div class="help-link">CLICK HERE FOR MORE INFO <svg width="11" height="11" viewBox="0 0 12 12" fill="none" stroke="#a3c63a" stroke-width="1.5"><circle cx="6" cy="6" r="5"/><path d="M5 4l2 2-2 2"/></svg></div></div>
</div>
<div class="abs help-item" style="left:822px;top:1579px">
  <div class="help-icon"><svg width="28" height="26" viewBox="0 0 28 26" fill="none" stroke="#aaa" stroke-width="2.5"><circle cx="10" cy="15" r="5" stroke-dasharray="3 2"/><circle cx="10" cy="15" r="2"/><circle cx="21" cy="7" r="4" stroke-dasharray="2.5 1.5"/></svg></div>
  <div><div class="help-text">Create Stronger, More Productive Teams</div><div class="help-link">CLICK HERE FOR MORE INFO <svg width="11" height="11" viewBox="0 0 12 12" fill="none" stroke="#a3c63a" stroke-width="1.5"><circle cx="6" cy="6" r="5"/><path d="M5 4l2 2-2 2"/></svg></div></div>
</div>
<div class="abs help-item" style="left:86px;top:1735px">
  <div class="help-icon"><svg width="22" height="26" viewBox="0 0 22 26" fill="none" stroke="#aaa" stroke-width="1.6"><path d="M2 1h12l6 6v18H2z"/><path d="M14 1v6h6M6 13h10M6 17h10M6 21h7"/></svg></div>
  <div><div class="help-text">Build Better Communications Pathways</div><div class="help-link">CLICK HERE FOR MORE INFO <svg width="11" height="11" viewBox="0 0 12 12" fill="none" stroke="#a3c63a" stroke-width="1.5"><circle cx="6" cy="6" r="5"/><path d="M5 4l2 2-2 2"/></svg></div></div>
</div>
<div class="abs help-item" style="left:454px;top:1735px">
  <div class="help-icon"><svg width="26" height="26" viewBox="0 0 26 26" fill="none" stroke="#aaa" stroke-width="2"><path d="M21 14v9H3V5h12"/><path d="M8 12l5 5L25 3"/></svg></div>
  <div><div class="help-text">Encourage Innovation &amp; Positive Change</div><div class="help-link">CLICK HERE FOR MORE INFO <svg width="11" height="11" viewBox="0 0 12 12" fill="none" stroke="#a3c63a" stroke-width="1.5"><circle cx="6" cy="6" r="5"/><path d="M5 4l2 2-2 2"/></svg></div></div>
</div>
<div class="abs help-item" style="left:822px;top:1735px">
  <div class="help-icon"><svg width="26" height="24" viewBox="0 0 26 24" fill="#aaa"><rect x="1" y="0" width="1.5" height="23"/><rect x="1" y="22" width="25" height="1.5"/><rect x="6" y="12" width="3" height="10"/><rect x="11" y="6" width="3" height="16"/><rect x="16" y="9" width="3" height="13"/><rect x="21" y="3" width="3" height="19"/></svg></div>
  <div><div class="help-text">Develop and Retain Strong Company Culture</div><div class="help-link">CLICK HERE FOR MORE INFO <svg width="11" height="11" viewBox="0 0 12 12" fill="none" stroke="#a3c63a" stroke-width="1.5"><circle cx="6" cy="6" r="5"/><path d="M5 4l2 2-2 2"/></svg></div></div>
</div>

<section class="abs contact"></section>
<h2 class="abs section-title" style="top:1912px">CONTACT US</h2>
<p class="abs section-sub" style="top:1957px">Our automated algorithms provide insights into the roles individuals play within the team beyond their titles.</p>
<div class="abs map" role="img" aria-label="Street map showing the office location"></div>
<p class="abs contact-intro">Lorem ipsum dolor sit amet, consectetur adipiscing elit, sed do eiusmod tempor inci did unt ut labore et dolore magna aliqua. Ut enim ad minim veniam, quis nostrud exercitatio ullamco laboris nisi ut aliquip ex ea commodo consequat.</p>

<div class="abs" style="left:622px;top:2100px">
  <h4 class="contact-head">ADDRESS</h4>
  <p class="contact-line" style="margin-top:8px"># 2547 Lorem Ipsum Dummy<br>Lorem Ipsum Dummy</p>
</div>
<div class="abs" style="left:874px;top:2100px">
  <h4 class="contact-head">EMAIL ADDRESS</h4>
  <p class="contact-line" style="margin-top:8px">General : info@company.com<br>Office :contact@company.com</p>
</div>
<div class="abs" style="left:622px;top:2218px">
  <h4 class="contact-head">PHONE</h4>
  <p class="contact-line" style="margin-top:8px">Mobile : (000)-121-1231</p>
</div>
<h4 class="abs contact-head" style="left:874px;top:2200px">FOLLOW US</h4>
<div class="abs social" aria-label="Social media links"><span></span><span></span><span></span><span></span><span></span></div>

<footer class="abs site-footer">© Copyright 2016. TEAMPRISMLY.All Rights Reserved</footer>

</body>
</html>
```